Maple Ridge business card design

Card needs to include the following text/items:
Company Logo
Tobin Marsh
Phone # - 555-318-7642
service@mapleridgelandscaping.example
Lawn & landscape maintenance services

```html
<!DOCTYPE html>
<html lang="en">
<head>
<meta charset="utf-8">
<title>Maple Ridge Landscaping – Business Card</title>
<link href="https://fonts.googleapis.com/css2?family=Montserrat:wght@400;700&display=swap" rel="stylesheet">
<style>
  :root {
    --forest: #214a2b;
    --olive: #7b9a45;
    --ink: #111111;
    --rule: #b9bdb9;
    --rule-green: #8fa58f;
    --paper: #ffffff;
    --frame: #1a1a1a;
  }
  * { box-sizing: border-box; margin: 0; padding: 0; }
  html, body {
    width: 1200px; height: 1000px; overflow: hidden;
    background: var(--paper);
    font-family: "Montserrat", Arial, sans-serif;
    color: var(--ink);
  }
  .canvas { position: relative; width: 1200px; height: 1000px; }
  .card {
    position: absolute; left: 211px; width: 778px; height: 445px;
    border: 1px solid var(--frame); background: var(--paper); overflow: hidden;
  }
  .card--front { top: 29px; }
  .card--back { top: 526px; }

  .brand { position: absolute; left: 0; right: 0; text-align: center; color: var(--forest); font-weight: 700; }
  .brand__mark {
    display: block; margin: 0 auto; border-radius: 50%;
    border: 4px solid var(--olive);
  }
  .brand__name { display: block; line-height: 1; letter-spacing: 0.5px; }
  .brand__tag { display: block; line-height: 1; text-transform: uppercase; }

  .card--front .brand { top: 94px; }
  .card--front .brand__mark { width: 220px; height: 220px; }
  .card--front .brand__name { font-size: 44px; margin-top: 8px; }
  .card--front .brand__tag { font-size: 17px; letter-spacing: 11px; margin-top: 8px; padding-left: 11px; }

  .card--back .brand { top: 34px; }
  .card--back .brand__mark { width: 136px; height: 136px; border-width: 3px; }
  .card--back .brand__name { font-size: 27px; margin-top: 6px; }
  .card--back .brand__tag { font-size: 11px; letter-spacing: 7px; margin-top: 4px; padding-left: 7px; }

  .person__name {
    position: absolute; top: 224px; left: 0; right: 0; text-align: center;
    font-size: 23px; font-weight: 700;
  }
  .person__role {
    position: absolute; top: 258px; left: 50px; right: 50px;
    display: flex; align-items: center; gap: 14px;
    font-size: 17px;
  }
  .person__role::before, .person__role::after {
    content: ""; flex: 1; height: 1px; background: var(--rule);
  }
  .contacts {
    position: absolute; top: 294px; left: 80px;
    display: flex; align-items: center; font-size: 17px;
  }
  .contacts__item { display: flex; align-items: center; }
  .contacts__item svg { width: 24px; height: 24px; margin-right: 24px; }
  .contacts__item--phone { margin-right: 58px; }
  .divider {
    position: absolute; top: 337px; left: 50px; right: 50px;
    height: 1px; background: var(--rule-green);
  }
  .tagline-band {
    position: absolute; top: 374px; left: 0; right: 0; height: 55px;
    background: var(--forest); color: var(--paper);
    display: flex; align-items: center; justify-content: center;
    font-size: 17px;
  }
</style>
</head>
<body>
<main class="canvas">
  <section class="card card--front">
    <div class="brand">
      <span class="brand__mark" aria-hidden="true"></span>
      <span class="brand__name">Maple Ridge</span>
      <span class="brand__tag">Landscaping</span>
    </div>
  </section>

  <section class="card card--back">
    <div class="brand">
      <span class="brand__mark" aria-hidden="true"></span>
      <span class="brand__name">Maple Ridge</span>
      <span class="brand__tag">Landscaping</span>
    </div>
    <h1 class="person__name">Tobin Marsh</h1>
    <p class="person__role">Owner</p>
    <div class="contacts">
      <span class="contacts__item contacts__item--phone">
        <svg viewBox="0 0 24 24" fill="none" stroke="#111" stroke-width="1.5" stroke-linejoin="round" aria-hidden="true">
          <path d="M6.5 3.5l3 3.2-1.8 2.3c1.2 2.6 3.2 4.6 5.8 5.8l2.3-1.8 3.2 3-1.8 2.8c-.5.6-1.3.9-2 .7C9.6 18 5.9 14.3 4.4 8.8c-.2-.7.1-1.5.7-2z"/>
        </svg>
        555-318-7642
      </span>
      <span class="contacts__item">
        <svg viewBox="0 0 24 24" fill="none" stroke="#111" stroke-width="1.6" stroke-linejoin="round" aria-hidden="true">
          <rect x="2.5" y="5.5" width="19" height="13" rx="1"/>
          <path d="M3 6.5l9 7 9-7"/>
        </svg>
        service@mapleridgelandscaping.example
      </span>
    </div>
    <div class="divider"></div>
    <p class="tagline-band">Lawn &amp; landscape maintenance services</p>
  </section>
</main>
</body>
</html>
```